New locally owned rental company needs a flyer to circulate

Need flyer with logo, phone# and address. We rent cars to anyone with driver's license and proper insurance. Rates as low as $50/day. Can offer compact cars, mid-size and full size sedans. Also SUV's.

```html
<!DOCTYPE html>
<html lang="en">
<head>
<meta charset="utf-8">
<title>DriveSoon Car &amp; Van Rental Flyer</title>
<link href="https://fonts.googleapis.com/css2?family=Bebas+Neue&family=Archivo+Black&family=Montserrat:wght@500;600;800&display=swap" rel="stylesheet">
<style>
  :root{
    --navy-deep:#061431;
    --navy:#0b1f5c;
    --blue:#0a5cab;
    --blue-light:#1b74c2;
    --band:#0653b0;
    --green:#2fb457;
    --white:#ffffff;
    --red:#b3121f;
  }
  *{margin:0;padding:0;box-sizing:border-box}
  html,body{width:849px;height:1200px;overflow:hidden;background:#e8e8e8}
  .flyer{position:relative;width:849px;height:1200px;overflow:hidden;background:var(--blue)}
  .backdrop{position:absolute;inset:0;width:849px;height:1200px}
  .brand{position:absolute;left:44px;top:168px;width:540px;text-align:center}
  .brand-name{font-family:'Montserrat',sans-serif;font-weight:800;font-size:72px;line-height:1;color:var(--white);letter-spacing:-1px}
  .brand-tagline{margin-top:18px;font-family:'Archivo Black',sans-serif;font-style:italic;font-size:26px;letter-spacing:14px;color:var(--white)}
  .price-badge{position:absolute;left:553px;top:365px;width:250px;height:250px;border-radius:50%;background:var(--green);color:var(--white);text-align:center;font-family:'Bebas Neue',sans-serif}
  .price-amount{display:block;font-size:132px;line-height:1;margin-top:32px;letter-spacing:-2px}
  .price-term{display:block;font-size:44px;line-height:1;margin-top:-10px;font-style:italic}
  .car-photo{position:absolute;left:40px;top:540px;width:790px;height:380px;border-radius:45% 50% 30% 30%;background:radial-gradient(ellipse at 55% 50%,#c4202c 0%,#9c0f1a 45%,rgba(120,10,20,.35) 70%,rgba(120,10,20,0) 78%)}
  .offer{position:absolute;left:0;width:849px;text-align:center;font-family:'Bebas Neue',sans-serif}
  .offer-main{top:930px;font-size:64px;line-height:1;color:var(--white)}
  .offer-sub{top:997px;font-size:43px;line-height:1;color:var(--green)}
  .contact{position:absolute;display:flex;align-items:center;color:var(--white);font-family:'Montserrat',sans-serif}
  .icon{width:46px;height:46px;border-radius:50%;background:var(--white);display:flex;align-items:center;justify-content:center;flex:none}
  .contact-phone{left:38px;top:1114px;font-size:34px;font-weight:500}
  .contact-phone .icon{margin-right:18px}
  .contact-address{left:460px;top:1132px;font-size:13px;font-weight:600;line-height:1.45}
  .contact-address .icon{margin-right:20px}
</style>
</head>
<body>
<main class="flyer">
  <svg class="backdrop" viewBox="0 0 849 1200" preserveAspectRatio="none" aria-hidden="true">
    <defs>
      <radialGradient id="midGlow" cx="0.45" cy="0.5" r="0.6">
        <stop offset="0" stop-color="#2a86d6"/>
        <stop offset="1" stop-color="#0a55a3"/>
      </radialGradient>
      <linearGradient id="lowerDark" x1="0" y1="0" x2="1" y2="1">
        <stop offset="0" stop-color="#0e2478"/>
        <stop offset="1" stop-color="#050f2c"/>
      </linearGradient>
      <linearGradient id="lotTone" x1="0" y1="0" x2="0" y2="1">
        <stop offset="0" stop-color="#0c2a5c"/>
        <stop offset="1" stop-color="#040d1f"/>
      </linearGradient>
    </defs>
    <rect width="849" height="1200" fill="url(#midGlow)"/>
    <polygon points="0,652 849,872 849,1200 0,1200" fill="url(#lowerDark)"/>
    <polygon role="img" aria-label="Photo of rental sedans parked in front of the office" points="0,0 849,0 849,203 151,534 0,393" fill="url(#lotTone)"/>
    <polygon points="0,1065 335,1065 364,1104 849,1104 849,1200 0,1200" fill="var(--band)"/>
    <polygon points="335,1065 364,1104 437,1200 430,1200 358,1104 330,1065" fill="#1d6cc8" opacity=".6"/>
  </svg>

  <header class="brand">
    <div class="brand-name">DriveSoon</div>
    <div class="brand-tagline">Car &amp; Van Rental</div>
  </header>

  <div class="car-photo" role="img" aria-label="Photo of a red compact sedan available for rent"></div>

  <div class="price-badge">
    <span class="price-amount">$50</span>
    <span class="price-term">For 1 Day</span>
  </div>

  <h1 class="offer offer-main">We rent cars to anyone</h1>
  <p class="offer offer-sub">With driver's license and proper insurance.</p>

  <div class="contact contact-phone">
    <span class="icon">
      <svg width="26" height="26" viewBox="0 0 24 24" aria-hidden="true"><path fill="#0653b0" d="M6.6 10.8a15.1 15.1 0 0 0 6.6 6.6l2.2-2.2a1 1 0 0 1 1-.25 11.4 11.4 0 0 0 3.6.57 1 1 0 0 1 1 1V20a1 1 0 0 1-1 1A17 17 0 0 1 3 4a1 1 0 0 1 1-1h3.5a1 1 0 0 1 1 1c0 1.25.2 2.45.57 3.57a1 1 0 0 1-.25 1z"/></svg>
    </span>
    555-014-2290
  </div>

  <div class="contact contact-address">
    <span class="icon">
      <svg width="24" height="24" viewBox="0 0 24 24" aria-hidden="true"><path fill="#0653b0" d="M12 2a7 7 0 0 0-7 7c0 5.2 7 13 7 13s7-7.8 7-13a7 7 0 0 0-7-7zm0 9.5A2.5 2.5 0 1 1 12 6.5a2.5 2.5 0 0 1 0 5z"/></svg>
    </span>
    <span>4870 Harbor Ridge Road<br>Fairview, AL 35000</span>
  </div>
</main>
</body>
</html>
```